Modern, cutting edge crypto trading website.

I need a single-page website design, approximate 4-5 pages. I have included a screenshot of the inside of the current application for some reference for what it currently looks like. This is the public side of the application for not logged in users.

I am currently thinking about 3-5 sections of the page.
Menu at top is optional, these could be the sections of the site.
1. Above the fold cool, grabbing stuff.
2. What problem does this solve
3. Additional benefits
4. Pricing
5. Open to ideas! Well it's all open to ideas if you have ideas.

I am nervous about hiring designers, I am open to a further discussion for more work for additional money but I have to LIKE your design. So this could be considered a trial. I would like to continue to design the application itself and match everything together!

I really like the trendkite website.

Competitor websites:
https://7pillars.example/
https://www.trendkite.example/

Target Market(s)

Adults 25-50 mostly male,

Number of Pages Required

4 page

Colors

Designer to choose colors to be used in the design.

Requirements
Must have
• Modern design, clean lines, professional.
Nice to have
• Fun SVG stuff. Not for this price, but in the future.
Should not have
• Should not be cluttered OR too spacey. Quorble's website has too much open space sometimes.

```html
<!DOCTYPE html>
<html lang="en">
<head>
<meta charset="utf-8">
<title>Tide Signals — Landing Page Variants</title>
<link href="https://fonts.googleapis.com/css2?family=Montserrat:wght@300;400;500;600;700&family=Open+Sans:wght@400;600&display=swap" rel="stylesheet">
<style>
:root{
  --navy:#0d2a5e;
  --navy-deep:#0a1f47;
  --blue:#1e7fd0;
  --sky:#2a9be0;
  --sky-light:#4fb2ee;
  --ink:#1c1f2a;
  --muted:#6b7280;
  --line:#e6e8ee;
  --paper:#ffffff;
  --mist:#f4f5f8;
  --night:#111214;
  --night-deep:#0a0a0b;
}
*{margin:0;padding:0;box-sizing:border-box}
html,body{width:1200px;height:2400px;overflow:hidden;background:var(--paper)}
body{font-family:"Open Sans",Arial,sans-serif;color:var(--ink)}
.board{position:absolute;left:0;top:0;width:1288px;height:2576px;transform:scale(.93168);transform-origin:0 0}
.page{position:absolute;top:75px;width:575px;background:var(--paper);overflow:hidden;box-shadow:0 2px 10px rgba(10,30,70,.06)}
.page--full{left:50px;height:2425px;--youdo:1185px;--pricing:1690px;--stats:2060px;--footer:2200px}
.page--compact{left:662px;height:2183px;--youdo:1185px;--pricing:1450px;--stats:1820px;--footer:1958px}
.abs{position:absolute}
.h-font{font-family:Montserrat,Arial,sans-serif}

/* hero */
.hero{left:0;top:0;width:575px;height:300px}
.hero-bg{position:absolute;inset:0}
.brand{left:43px;top:27px;display:flex;align-items:center;gap:6px;color:#fff;font-family:Montserrat,sans-serif;font-weight:300;font-size:15px;letter-spacing:.5px;line-height:1}
.brand-dot{width:22px;height:22px;border:2px solid #fff;border-radius:50%}
.nav{left:187px;top:31px;display:flex;gap:19px;font-family:Montserrat,sans-serif;font-size:7px;font-weight:500;color:#fff}
.nav .active{color:var(--sky-light);border-bottom:1px solid var(--sky-light);padding-bottom:2px}
.btn{display:inline-flex;align-items:center;justify-content:center;border-radius:12px;background:var(--sky);color:#fff;font-family:Montserrat,sans-serif;font-weight:600;font-size:7px;letter-spacing:.3px}
.signup{left:472px;top:25px;width:60px;height:22px}
.hero-title{left:43px;top:100px;color:#fff;font-family:Montserrat,sans-serif;font-weight:600;font-size:26px}
.hero-copy{left:43px;top:135px;width:185px;color:#fff;font-size:7.5px;line-height:15px;font-weight:600}
.getstarted{left:43px;top:186px;width:60px;height:20px;border-radius:10px}
.laptop-screen{border:7px solid #1a1b1f;border-bottom-width:9px;border-radius:8px 8px 0 0;background:linear-gradient(160deg,#f7f8fa,#e3e7ee)}
.laptop-base{height:7px;border-radius:0 0 10px 10px;background:linear-gradient(#dfe2e7,#9ea3ab)}

/* partners */
.partners{left:43px;top:345px;width:490px;display:flex;justify-content:space-between;align-items:center;font-family:Montserrat,sans-serif;font-size:8.5px;font-weight:600;color:#7d828c}

/* about */
.about-art{left:58px;top:452px;width:130px;height:130px;border-radius:50%;background:radial-gradient(circle at 40% 40%,#2c6fe0,#0c2f8f 70%,#0a1f5a)}
.about-blob{left:0;top:400px;width:230px;height:150px;border-radius:0 90px 80px 0;background:#eef4fb}
.eyebrow{font-family:Montserrat,sans-serif;font-weight:500;font-size:7.5px;color:var(--ink)}
.section-title{font-family:Montserrat,sans-serif;font-size:16.5px;font-weight:300;color:var(--sky);letter-spacing:.3px}
.section-title b{font-weight:700;color:var(--blue)}
.body-copy{font-size:6.6px;line-height:16.3px;color:#4b5060}
.about-text{left:268px;top:423px;width:240px}
.about-text .section-title{margin-top:6px}
.about-text .body-copy{margin-top:6px}
.readmore{width:76px;height:22px;margin-top:14px}

/* strategy band */
.band{left:0;top:620px;width:575px;height:310px}
.band-text{left:307px;top:705px;width:240px;color:#fff}
.band-text .eyebrow,.band-text .section-title,.band-text .section-title b{color:#fff}
.band-text .section-title{margin-top:4px}
.band-text .body-copy{color:#e6f1fb;margin-top:6px;line-height:14px}
.band-text .btn{background:#1768bd;width:76px;height:22px;margin-top:18px}

/* steps */
.steps-head{left:0;top:972px;width:575px;text-align:center}
.steps-head .section-title{margin-top:3px}
.steps{left:43px;top:1020px;width:490px;display:flex;justify-content:space-between}
.step{width:150px;text-align:center}
.step-icon{width:48px;height:48px;margin:0 auto;border-radius:50%;background:var(--blue);display:flex;align-items:center;justify-content:center;box-shadow:0 4px 10px rgba(30,127,208,.25)}
.step h3{margin-top:17px;font-family:Montserrat,sans-serif;font-weight:500;font-size:7.6px}
.step p{margin-top:6px;font-size:6.3px;line-height:12.5px;color:#555a66}

/* you do / we do */
.youdo{left:0;top:var(--youdo);width:575px}
.row{position:relative;width:575px;height:250px;display:flex}
.cell{position:relative;width:50%;height:100%;padding:48px 0 0 43px;color:#fff}
.cell--sky{background:linear-gradient(135deg,#2fa2e6,#2190d8)}
.cell--blue{background:linear-gradient(135deg,#2182d3,#1a70c4)}
.cell--mist{background:var(--mist)}
.cell--white{background:var(--paper)}
.cell h2{font-family:Montserrat,sans-serif;font-size:16px;font-weight:300}
.cell h2 b{font-weight:700}
.thing{margin-top:12px}
.thing h4{font-size:7.5px;font-weight:400}
.thing p{font-size:6.4px;line-height:13px;width:210px;margin-top:4px;color:#e3f0fb}
.art{position:absolute;border-radius:6px}

/* pricing */
.pricing{left:0;top:var(--pricing);width:575px;height:320px}
.pricing-title{left:0;top:40px;width:575px;text-align:center;font-family:Montserrat,sans-serif;font-weight:600;font-size:14px;color:var(--ink)}
.pricing-rule{left:283px;top:66px;width:9px;height:2px;background:var(--navy)}
.plans{left:71px;top:101px;display:flex;gap:11px}
.plan{position:relative;width:137px;height:154px;background:#fff;box-shadow:0 3px 10px rgba(20,40,80,.07);text-align:center;padding-top:32px}
.price{position:absolute;left:46px;top:-24px;width:46px;height:46px;border-radius:50%;background:#fff;box-shadow:0 0 0 1px var(--line);display:flex;align-items:center;justify-content:center;font-family:Montserrat,sans-serif;font-size:12px;color:var(--ink)}
.price small{font-size:6px}
.plan h3{font-family:Montserrat,sans-serif;font-weight:400;font-size:10px}
.plan ul{list-style:none;margin:10px 15px 0}
.plan li{font-size:6.6px;color:#777;padding:6px 0;border-bottom:1px solid var(--line)}
.plan .btn{position:absolute;left:34px;bottom:-10px;width:70px;height:22px}

/* stats */
.stats{left:71px;top:var(--stats);width:434px;display:flex}
.stat{width:108.5px;text-align:center;border-right:1px solid var(--line);padding:4px 0}
.stat:last-child{border-right:0}
.stat b{display:block;margin-top:10px;font-family:Montserrat,sans-serif;font-size:8px;color:var(--blue)}
.stat span{display:block;font-size:6px;color:#666;margin-top:2px}

/* footer */
.footer{left:0;top:var(--footer);width:575px;height:225px;color:#fff}
.foot-col{position:absolute;top:55px}
.foot-col h3{font-family:Montserrat,sans-serif;font-weight:500;font-size:12px}
.foot-col p,.foot-col li{font-size:5.5px;line-height:13px;list-style:none}
.foot-col .first{margin-top:10px}
.subscribe{margin-top:8px;width:133px;height:17px;border-radius:9px;background:#fff;border:1px solid var(--sky);display:flex;align-items:center;justify-content:space-between;padding-left:7px;font-size:5px;color:#999}
.subscribe span{height:15px;width:50px;border-radius:8px;background:var(--sky);color:#fff;display:flex;align-items:center;justify-content:center;font-family:Montserrat,sans-serif;font-weight:600}
.socials{display:flex;gap:9px;margin-top:16px}
.socials i{width:7px;height:7px;border-radius:50%;background:#fff;display:block}
.foot-btn{position:absolute;left:441px;width:91px;height:22px;border-radius:11px;font-family:Montserrat,sans-serif;font-size:6.3px;font-weight:600;display:flex;align-items:center;justify-content:center}
.foot-btn--ghost{top:58px;background:#fff;color:var(--sky)}
.foot-btn--solid{top:86px;background:var(--sky);color:#fff}
.copyright{position:absolute;left:0;bottom:0;width:575px;height:25px;background:var(--night-deep);text-align:center;font-size:5px;line-height:25px;color:#ddd}
</style>
</head>
<body>
<div class="board">

  <!-- ============ Variant A ============ -->
  <section class="page page--full">
    <div class="abs hero">
      <svg class="hero-bg" width="575" height="300" viewBox="0 0 575 300" role="img" aria-label="Dark blue trading chart backdrop">
        <defs>
          <linearGradient id="heroA" x1="0" y1="0" x2="1" y2="1">
            <stop offset="0" stop-color="#163a78"/><stop offset=".6" stop-color="#0d2a5e"/><stop offset="1" stop-color="#123f86"/>
          </linearGradient>
        </defs>
        <path d="M0 0H575V255C545 250 520 300 440 300C360 300 200 285 0 278Z" fill="url(#heroA)"/>
        <path d="M0 278C200 285 360 300 440 300C380 304 200 300 0 300Z" fill="#ffffff"/>
      </svg>
      <div class="abs brand"><span class="brand-dot"></span>TIDE SIGNALS</div>
      <nav class="abs nav"><span class="active">Home</span><span>About Us</span><span>Benefits</span><span>Pricing</span><span>Blog</span><span>Contact</span></nav>
      <div class="abs btn signup">Sign Up</div>
      <h1 class="abs hero-title">Tide Signals</h1>
      <p class="abs hero-copy">Etiam varius eros aliquam semper rhoncus molestie velit sit amet ligula accumsan, eu vehicula sem consequat..</p>
      <div class="abs btn getstarted">Get Started</div>
      <div class="abs laptop-screen" style="left:255px;top:73px;width:268px;height:180px" role="img" aria-label="App dashboard showing the strategies table"></div>
      <div class="abs laptop-base" style="left:225px;top:253px;width:328px"></div>
    </div>

    <div class="abs partners"><span>MAHALO WORKS</span><span>TALLYLINE</span><span>PLACEHOLDER CO</span><span>Glad Patron</span><span>PARLANCE</span></div>

    <div class="abs about-blob"></div>
    <div class="abs about-art" role="img" aria-label="Isometric crypto server network illustration"></div>
    <div class="abs about-text">
      <div class="eyebrow">About Us</div>
      <h2 class="section-title">TIDE <b>SIGNALS</b></h2>
      <p class="body-copy">Lorem ipsum dolor sit amet, consectetur adipiscing elit, sed do eiusmod tempor incididunt ut labore et dolore magna aliqua. Ut enim ad minim veniam, quis nostrud exercitation ullamco laboris nisi ut aliquip ex ea commodo consequat. Duis aute irure dolor in reprehenderit in voluptate velit esse cillum dolore eu fugiat nulla pariatur.</p>
      <div class="btn readmore">READ MORE</div>
    </div>

    <svg class="abs band" viewBox="0 0 575 310">
      <defs><linearGradient id="bandA" x1="0" y1="0" x2="1" y2="0"><stop offset="0" stop-color="#1a73c9"/><stop offset="1" stop-color="#2592dd"/></linearGradient></defs>
      <path d="M0 8Q300 -8 575 5V288Q300 320 0 290Z" fill="url(#bandA)"/>
    </svg>
    <div class="abs laptop-screen" style="left:-7px;top:662px;width:268px;height:222px;border-radius:0 8px 0 0" role="img" aria-label="App screen showing strategy editor"></div>
    <div class="abs laptop-base" style="left:0;top:884px;width:292px;border-radius:0 0 12px 0"></div>
    <div class="abs band-text">
      <div class="eyebrow">Strategy New</div>
      <h2 class="section-title">WHAT <b>WE DO</b></h2>
      <p class="body-copy">Lorem ipsum dolor sit amet, consectetur adipiscing elit, sed do eiusmod tempor incididunt ut labore et dolore magna aliqua. Ut enim ad minim veniam, quis nostrud exercitation ullamco laboris nisi ut aliquip ex ea</p>
      <div class="btn">READ MORE</div>
    </div>

    <div class="abs steps-head">
      <div class="eyebrow">Tide Signals</div>
      <h2 class="section-title">HOW TO <b>GET STARTED</b></h2>
    </div>
    <div class="abs steps">
      <div class="step"><div class="step-icon"><svg width="20" height="20" fill="none" stroke="#fff" stroke-width="1.3"><rect x="2" y="3" width="16" height="13" rx="1"/><path d="M5 8h10M5 11h7"/></svg></div><h3>Connect Exchange</h3><p>Lorem ipsum dolor sit amet, consectetur adipiscing elit, sed do eiusmod tempor Lorem ipsum dolor sit amet...</p></div>
      <div class="step"><div class="step-icon"><svg width="20" height="20" fill="none" stroke="#fff" stroke-width="1.3"><rect x="2" y="3" width="16" height="12" rx="1"/><path d="M5 12l3-3 3 2 4-5"/></svg></div><h3>Create or Select Strategy</h3><p>Lorem ipsum dolor sit amet, consectetur adipiscing elit, sed do eiusmod tempor Lorem ipsum dolor sit amet...</p></div>
      <div class="step"><div class="step-icon"><svg width="20" height="20" fill="none" stroke="#fff" stroke-width="1.3"><circle cx="10" cy="10" r="7"/><path d="M7 10h6M10 7v6"/></svg></div><h3>Automatically Rebalance</h3><p>Lorem ipsum dolor sit amet, consectetur adipiscing elit, sed do eiusmod tempor Lorem ipsum dolor sit amet...</p></div>
    </div>

    <div class="abs youdo">
      <div class="row">
        <div class="cell cell--sky"><h2>YOU <b>DO</b></h2>
          <div class="thing"><h4>Thing 1</h4><p>Lorem ipsum dolor sit amet, consectetur adipiscing elit, sed do etempor incididunt ut labore et dolore magna aliqua.</p></div>
          <div class="thing"><h4>Thing 2</h4><p>Lorem ipsum dolor sit amet, consectetur adipiscing elit, sed do etempor incididunt ut labore et dolore magna aliqua.</p></div>
          <div class="thing"><h4>Thing 3</h4><p>Lorem ipsum dolor sit amet, consectetur adipiscing elit, sed do etempor incididunt ut labore et dolore magna aliqua.</p></div>
        </div>
        <div class="cell cell--mist"><div class="art" style="left:12px;top:40px;width:262px;height:170px;background:radial-gradient(ellipse at center,#2b6fe0 0%,#6aa3ee 45%,rgba(242,244,247,0) 72%)" role="img" aria-label="Isometric crypto trading platform illustration"></div></div>
      </div>
      <div class="row">
        <div class="cell cell--white"><div class="art" style="left:20px;top:35px;width:250px;height:180px;background:radial-gradient(ellipse at center,#2a62d8 0%,#67c6e6 45%,rgba(255,255,255,0) 72%)" role="img" aria-label="Isometric data center and blockchain illustration"></div></div>
        <div class="cell cell--blue"><h2>WE <b>DO</b></h2>
          <div class="thing"><h4>Thing 1</h4><p>Lorem ipsum dolor sit amet, consectetur adipiscing elit, sed do etempor incididunt ut labore et dolore magna aliqua.</p></div>
          <div class="thing"><h4>Thing 2</h4><p>Lorem ipsum dolor sit amet, consectetur adipiscing elit, sed do etempor incididunt ut labore et dolore magna aliqua.</p></div>
          <div class="thing"><h4>Thing 3</h4><p>Lorem ipsum dolor sit amet, consectetur adipiscing elit, sed do etempor incididunt ut labore et dolore magna aliqua.</p></div>
        </div>
      </div>
    </div>

    <div class="abs pricing">
      <svg class="abs" style="left:0;top:0" width="575" height="320"><path d="M0 0H575V300Q300 325 0 312Z" fill="#f4f5f8"/></svg>
      <h2 class="abs pricing-title">Pricing</h2>
      <div class="abs pricing-rule"></div>
      <div class="abs plans">
        <div class="plan"><div class="price">$99/<small>mn</small></div><h3>Basic</h3><ul><li>Lorem ipsum dolor sit amet</li><li>Lorem ipsum dolor sit amet</li><li>Lorem ipsum dolor sit amet</li></ul><div class="btn">BUY NOW</div></div>
        <div class="plan"><div class="price">$129/<small>mn</small></div><h3>Standard</h3><ul><li>Lorem ipsum dolor sit amet</li><li>Lorem ipsum dolor sit amet</li><li>Lorem ipsum dolor sit amet</li></ul><div class="btn">BUY NOW</div></div>
        <div class="plan"><div class="price">$288/<small>mn</small></div><h3>Premium</h3><ul><li>Lorem ipsum dolor sit amet</li><li>Lorem ipsum dolor sit amet</li><li>Lorem ipsum dolor sit amet</li></ul><div class="btn">BUY NOW</div></div>
      </div>
    </div>

    <div class="abs stats">
      <div class="stat"><svg width="16" height="14" fill="none" stroke="#2a9be0"><path d="M2 13h13M4 12V8M7 12V6M10 12V4M13 12V7"/></svg><b>50M+</b><span>Trading Volume (USD)</span></div>
      <div class="stat"><svg width="16" height="14" fill="none" stroke="#2a9be0"><rect x="4" y="3" width="8" height="8"/><path d="M6 1v2M10 1v2M6 11v2M10 11v2M2 5h2M2 9h2M12 5h2M12 9h2"/></svg><b>300K</b><span>Transactions</span></div>
      <div class="stat"><svg width="16" height="14" fill="none" stroke="#2a9be0"><rect x="3" y="1" width="8" height="11"/><path d="M5 4h4M5 7h4"/><circle cx="12" cy="10" r="2.5"/></svg><b>40K+</b><span>Happy Users</span></div>
      <div class="stat"><svg width="16" height="14" fill="none" stroke="#2a9be0"><rect x="2" y="2" width="12" height="10"/><path d="M4 10l3-3 2 2 4-4"/></svg><b>10K+</b><span>Custom Portfolios Created</span></div>
    </div>

    <div class="abs footer">
      <svg class="abs" style="left:0;top:0" width="575" height="225"><path d="M0 10Q290 -8 575 15V225H0Z" fill="#111214"/></svg>
      <div class="foot-col" style="left:43px"><h3>Links</h3><ul class="first"><li>Home</li><li>About Us</li><li>Solution</li><li>Benefits</li><li>Pricing</li><li>Blog</li><li>Contact Us</li></ul></div>
      <div class="foot-col" style="left:126px"><h3>Contact Us</h3><div class="first"><p>At vero eos et accusamus 1F Brookvale, PA 10000</p><p>Ph: 555-014-2298 310</p><p>hello@tidesignals.example</p></div></div>
      <div class="foot-col" style="left:270px"><h3>Newsletter</h3><p class="first">Subscribe Our Newsletter For More Info</p><div class="subscribe">Email Address<span>SUBSCRIBE</span></div><div class="socials"><i></i><i></i><i></i><i></i></div></div>
      <div class="foot-btn foot-btn--ghost">SIGN IN</div>
      <div class="foot-btn foot-btn--solid">CREATE ACCOUNT</div>
      <div class="copyright">© 2019 Copyrights.The Company Name.All Rights Reserved</div>
    </div>
  </section>

  <!-- ============ Variant B ============ -->
  <section class="page page--compact">
    <div class="abs hero">
      <svg class="hero-bg" width="575" height="300" viewBox="0 0 575 300" role="img" aria-label="Dark blue trading chart backdrop">
        <defs>
          <linearGradient id="heroB" x1="0" y1="0" x2="1" y2="1">
            <stop offset="0" stop-color="#163a78"/><stop offset=".6" stop-color="#0d2a5e"/><stop offset="1" stop-color="#123f86"/>
          </linearGradient>
        </defs>
        <path d="M0 0H575V255C545 250 520 300 440 300C360 300 200 285 0 278Z" fill="url(#heroB)"/>
      </svg>
      <div class="abs brand"><span class="brand-dot"></span>TIDE SIGNALS</div>
      <nav class="abs nav"><span class="active">Home</span><span>About Us</span><span>Benefits</span><span>Pricing</span><span>Blog</span><span>Contact</span></nav>
      <div class="abs btn signup">Sign Up</div>
      <h1 class="abs hero-title">Tide Signals</h1>
      <p class="abs hero-copy">Etiam varius eros aliquam semper rhoncus molestie velit sit amet ligula accumsan, eu vehicula sem consequat..</p>
      <div class="abs btn getstarted">Get Started</div>
      <div class="abs laptop-screen" style="left:255px;top:73px;width:268px;height:180px" role="img" aria-label="App dashboard showing the strategies table"></div>
      <div class="abs laptop-base" style="left:225px;top:253px;width:328px"></div>
    </div>

    <div class="abs partners"><span>MAHALO WORKS</span><span>TALLYLINE</span><span>PLACEHOLDER CO</span><span>Glad Patron</span><span>PARLANCE</span></div>

    <div class="abs about-blob"></div>
    <div class="abs about-art" role="img" aria-label="Isometric crypto server network illustration"></div>
    <div class="abs about-text">
      <div class="eyebrow">About Us</div>
      <h2 class="section-title">TIDE <b>SIGNALS</b></h2>
      <p class="body-copy">Lorem ipsum dolor sit amet, consectetur adipiscing elit, sed do eiusmod tempor incididunt ut labore et dolore magna aliqua. Ut enim ad minim veniam, quis nostrud exercitation ullamco laboris nisi ut aliquip ex ea commodo consequat. Duis aute irure dolor in reprehenderit in voluptate velit esse cillum dolore eu fugiat nulla pariatur.</p>
      <div class="btn readmore">READ MORE</div>
    </div>

    <svg class="abs band" viewBox="0 0 575 310">
      <defs><linearGradient id="bandB" x1="0" y1="0" x2="1" y2="0"><stop offset="0" stop-color="#1a73c9"/><stop offset="1" stop-color="#2592dd"/></linearGradient></defs>
      <path d="M0 8Q300 -8 575 5V288Q300 320 0 290Z" fill="url(#bandB)"/>
    </svg>
    <div class="abs laptop-screen" style="left:-7px;top:662px;width:268px;height:222px;border-radius:0 8px 0 0" role="img" aria-label="App screen showing strategy editor"></div>
    <div class="abs laptop-base" style="left:0;top:884px;width:292px;border-radius:0 0 12px 0"></div>
    <div class="abs band-text">
      <div class="eyebrow">Strategy New</div>
      <h2 class="section-title">WHAT <b>WE DO</b></h2>
      <p class="body-copy">Lorem ipsum dolor sit amet, consectetur adipiscing elit, sed do eiusmod tempor incididunt ut labore et dolore magna aliqua. Ut enim ad minim veniam, quis nostrud exercitation ullamco laboris nisi ut aliquip ex ea</p>
      <div class="btn">READ MORE</div>
    </div>

    <div class="abs steps-head">
      <div class="eyebrow">Tide Signals</div>
      <h2 class="section-title">HOW TO <b>GET STARTED</b></h2>
    </div>
    <div class="abs steps">
      <div class="step"><div class="step-icon"><svg width="20" height="20" fill="none" stroke="#fff" stroke-width="1.3"><rect x="2" y="3" width="16" height="13" rx="1"/><path d="M5 8h10M5 11h7"/></svg></div><h3>Connect Exchange</h3><p>Lorem ipsum dolor sit amet, consectetur adipiscing elit, sed do eiusmod tempor Lorem ipsum dolor sit amet...</p></div>
      <div class="step"><div class="step-icon"><svg width="20" height="20" fill="none" stroke="#fff" stroke-width="1.3"><rect x="2" y="3" width="16" height="12" rx="1"/><path d="M5 12l3-3 3 2 4-5"/></svg></div><h3>Create or Select Strategy</h3><p>Lorem ipsum dolor sit amet, consectetur adipiscing elit, sed do eiusmod tempor Lorem ipsum dolor sit amet...</p></div>
      <div class="step"><div class="step-icon"><svg width="20" height="20" fill="none" stroke="#fff" stroke-width="1.3"><circle cx="10" cy="10" r="7"/><path d="M7 10h6M10 7v6"/></svg></div><h3>Automatically Rebalance</h3><p>Lorem ipsum dolor sit amet, consectetur adipiscing elit, sed do eiusmod tempor Lorem ipsum dolor sit amet...</p></div>
    </div>

    <div class="abs youdo">
      <div class="row" style="height:262px">
        <div class="cell cell--sky"><h2>YOU <b>DO</b></h2>
          <div class="thing"><h4>Thing 1</h4><p>Lorem ipsum dolor sit amet, consectetur adipiscing elit, sed do etempor incididunt ut labore et dolore magna aliqua.</p></div>
          <div class="thing"><h4>Thing 2</h4><p>Lorem ipsum dolor sit amet, consectetur adipiscing elit, sed do etempor incididunt ut labore et dolore magna aliqua.</p></div>
          <div class="thing"><h4>Thing 3</h4><p>Lorem ipsum dolor sit amet, consectetur adipiscing elit, sed do etempor incididunt ut labore et dolore magna aliqua.</p></div>
        </div>
        <div class="cell cell--blue"><h2>WE <b>DO</b></h2>
          <div class="thing"><h4>Thing 1</h4><p>Lorem ipsum dolor sit amet, consectetur adipiscing elit, sed do etempor incididunt ut labore et dolore magna aliqua.</p></div>
          <div class="thing"><h4>Thing 2</h4><p>Lorem ipsum dolor sit amet, consectetur adipiscing elit, sed do etempor incididunt ut labore et dolore magna aliqua.</p></div>
          <div class="thing"><h4>Thing 3</h4><p>Lorem ipsum dolor sit amet, consectetur adipiscing elit, sed do etempor incididunt ut labore et dolore magna aliqua.</p></div>
        </div>
      </div>
    </div>

    <div class="abs pricing">
      <svg class="abs" style="left:0;top:0" width="575" height="320"><path d="M0 0H575V300Q300 325 0 312Z" fill="#f4f5f8"/></svg>
      <h2 class="abs pricing-title">Pricing</h2>
      <div class="abs pricing-rule"></div>
      <div class="abs plans">
        <div class="plan"><div class="price">$99/<small>mn</small></div><h3>Basic</h3><ul><li>Lorem ipsum dolor sit amet</li><li>Lorem ipsum dolor sit amet</li><li>Lorem ipsum dolor sit amet</li></ul><div class="btn">BUY NOW</div></div>
        <div class="plan"><div class="price">$129/<small>mn</small></div><h3>Standard</h3><ul><li>Lorem ipsum dolor sit amet</li><li>Lorem ipsum dolor sit amet</li><li>Lorem ipsum dolor sit amet</li></ul><div class="btn">BUY NOW</div></div>
        <div class="plan"><div class="price">$288/<small>mn</small></div><h3>Premium</h3><ul><li>Lorem ipsum dolor sit amet</li><li>Lorem ipsum dolor sit amet</li><li>Lorem ipsum dolor sit amet</li></ul><div class="btn">BUY NOW</div></div>
      </div>
    </div>

    <div class="abs stats">
      <div class="stat"><svg width="16" height="14" fill="none" stroke="#2a9be0"><path d="M2 13h13M4 12V8M7 12V6M10 12V4M13 12V7"/></svg><b>50M+</b><span>Trading Volume (USD)</span></div>
      <div class="stat"><svg width="16" height="14" fill="none" stroke="#2a9be0"><rect x="4" y="3" width="8" height="8"/><path d="M6 1v2M10 1v2M6 11v2M10 11v2M2 5h2M2 9h2M12 5h2M12 9h2"/></svg><b>300K</b><span>Transactions</span></div>
      <div class="stat"><svg width="16" height="14" fill="none" stroke="#2a9be0"><rect x="3" y="1" width="8" height="11"/><path d="M5 4h4M5 7h4"/><circle cx="12" cy="10" r="2.5"/></svg><b>40K+</b><span>Happy Users</span></div>
      <div class="stat"><svg width="16" height="14" fill="none" stroke="#2a9be0"><rect x="2" y="2" width="12" height="10"/><path d="M4 10l3-3 2 2 4-4"/></svg><b>10K+</b><span>Custom Portfolios Created</span></div>
    </div>

    <div class="abs footer">
      <svg class="abs" style="left:0;top:0" width="575" height="225"><path d="M0 10Q290 -8 575 15V225H0Z" fill="#111214"/></svg>
      <div class="foot-col" style="left:43px"><h3>Links</h3><ul class="first"><li>Home</li><li>About Us</li><li>Solution</li><li>Benefits</li><li>Pricing</li><li>Blog</li><li>Contact Us</li></ul></div>
      <div class="foot-col" style="left:126px"><h3>Contact Us</h3><div class="first"><p>At vero eos et accusamus 1F Brookvale, PA 10000</p><p>Ph: 555-014-2298 310</p><p>hello@tidesignals.example</p></div></div>
      <div class="foot-col" style="left:270px"><h3>Newsletter</h3><p class="first">Subscribe Our Newsletter For More Info</p><div class="subscribe">Email Address<span>SUBSCRIBE</span></div><div class="socials"><i></i><i></i><i></i><i></i></div></div>
      <div class="foot-btn foot-btn--ghost">SIGN IN</div>
      <div class="foot-btn foot-btn--solid">CREATE ACCOUNT</div>
      <div class="copyright">© 2019 Copyrights.The Company Name.All Rights Reserved</div>
    </div>
  </section>

</div>
</body>
</html>
```